Founder / concept developer needs business card // Consultant needs VCARD

I need a business card for me as a founding consultant in Berlin. I advise entrepreneurs, especially in the design of business ideas, business plans or financing applications. More information about this in the annexes. My USP: I design / structure complex ideas and projects convincingly so that my client is successful. I want to communicate professionalism, effectiveness and clarity. Colors like from the range BLACK-GRAY-GREEN. I am 27 years old, I have studied business for 7 years. Attachments: - Business card design (only idea, do not focus on it) - Website screenshot (only idea, do not focus on it)

Target Market(s)

Target group: Founder (20-50 yrs, m / w, needy, in "break-up phase") and CONTRACTOR / "financier" (30-55 yrs, m / w, often public service "routine-oriented"). The foundations are in quite different industries: digital, craft, tourism, retail, services, etc. Almost all German.

Industry/Entity Type

Consultant

Contact Information for Business Card

Lukas Brenner
M. Sc., International Business Administration
Gründungsberater, Konzeptentwickler
www.falkor-plan.de
kontakt@falkor-plan.de
Tel. 0157 284 3361

Colors

Designer to choose colors to be used in the design.

Requirements
Must have
• Professionalism, persuasiveness, clarity
Nice to have
• memorability
Should not have
• Schnörkelei

```html
<!DOCTYPE html>
<html lang="de">
<head>
<meta charset="utf-8">
<title>Lukas Brenner – Visitenkarte</title>
<link rel="stylesheet" href="https://fonts.googleapis.com/css2?family=Open+Sans:wght@400;600;700&display=swap">
<style>
  :root {
    --stage: #1c1c1c;
    --card: #2a2a2a;
    --card-edge: #333333;
    --white: #ececec;
    --muted: #d6d6d6;
    --green: #3fa34d;
  }
  * { margin: 0; padding: 0; box-sizing: border-box; }
  html, body { width: 1200px; height: 716px; overflow: hidden; background: var(--stage); }
  body { font-family: "Open Sans", Arial, sans-serif; color: var(--white); }
  .canvas { position: relative; width: 1200px; height: 716px; }

  .card {
    position: absolute;
    top: 213px;
    width: 500px;
    height: 290px;
    background: var(--card);
    border: 1px solid var(--card-edge);
    border-radius: 22px;
  }
  .card--front { left: 60px; }
  .card--back { left: 640px; }

  /* Front */
  .front-brand {
    position: absolute;
    top: 110px; left: 0; right: 0;
    display: flex; align-items: center; justify-content: center; gap: 12px;
  }
  .brand-dot { width: 18px; height: 18px; border-radius: 50%; background: var(--green); }
  .brand-name { font-size: 26px; font-weight: 600; letter-spacing: 2px; color: var(--white); }
  .front-url {
    position: absolute; top: 168px; left: 0; right: 0;
    text-align: center; font-size: 13px; color: var(--green);
  }

  /* Back */
  .back-brand {
    position: absolute; top: 40px; right: 34px;
    display: flex; align-items: center; gap: 10px;
  }
  .back-brand .brand-name { font-size: 16px; letter-spacing: 1.5px; }
  .back-brand .brand-dot { width: 14px; height: 14px; }

  .holder { position: absolute; left: 30px; top: 130px; right: 30px; }
  .holder-name { font-size: 22px; font-weight: 400; color: var(--white); margin-bottom: 4px; }
  .holder-role { font-size: 14px; line-height: 1.3; color: var(--green); }
  .rule { height: 1.5px; background: var(--green); margin: 10px 0 10px; }
  .contact { display: flex; align-items: center; gap: 8px; font-size: 13px; color: var(--muted); white-space: nowrap; }
  .contact-item { display: flex; align-items: center; gap: 5px; }
  .contact-sep { color: var(--muted); }
  .icon { width: 13px; height: 13px; fill: var(--green); flex: none; }
</style>
</head>
<body>
<div class="canvas">

  <section class="card card--front" aria-label="Vorderseite">
    <div class="front-brand">
      <span class="brand-dot"></span>
      <span class="brand-name">LUKAS BRENNER</span>
    </div>
    <p class="front-url">www.falkor-plan.de</p>
  </section>

  <section class="card card--back" aria-label="Rückseite">
    <div class="back-brand">
      <span class="brand-dot"></span>
      <span class="brand-name">LUKAS BRENNER</span>
    </div>

    <div class="holder">
      <h1 class="holder-name">Lukas Brenner</h1>
      <p class="holder-role">M. Sc., International Business Administration<br>Gründungsberater, Konzeptentwickler</p>
      <div class="rule"></div>
      <div class="contact">
        <span class="contact-item">
          <svg class="icon" viewBox="0 0 16 16" aria-hidden="true"><path d="M1 5c0-2 3-3 7-3s7 1 7 3v1h-3.5V4.5h-7V6H1zM4 7h8l2.5 3v4h-13v-4zM8 9a1.8 1.8 0 1 0 0 3.6A1.8 1.8 0 0 0 8 9z"/></svg>
          0157 284 3361
        </span>
        <span class="contact-sep">|</span>
        <span class="contact-item">
          <svg class="icon" viewBox="0 0 16 16" aria-hidden="true"><path d="M1 3h14v10H1zM2.5 4.5 8 9l5.5-4.5z"/></svg>
          kontakt@falkor-plan.de
        </span>
        <span class="contact-sep">|</span>
        <span class="contact-item">
          <svg class="icon" viewBox="0 0 16 16" aria-hidden="true"><path d="M8 1a7 7 0 1 0 0 14A7 7 0 0 0 8 1zm0 1.5c.8 0 1.7 1.6 2 4H6c.3-2.4 1.2-4 2-4zM2.6 6.5h2c0 .5-.1 1-.1 1.5s0 1 .1 1.5h-2a5.6 5.6 0 0 1 0-3zm3.4 3h4c-.3 2.4-1.2 4-2 4s-1.7-1.6-2-4zm5.4 0c.1-.5.1-1 .1-1.5s0-1-.1-1.5h2a5.6 5.6 0 0 1 0 3z"/></svg>
          www.falkor-plan.de
        </span>
      </div>
    </div>
  </section>

</div>
</body>
</html>
```